One Page Website for Personal Trainer in London

I have a logo and need a one page website designed around my branding. I am a freelance Personal Trainer based in London specialising in bodyweight training for men and women. I would like the site to be modern and clean but not overtly urban in design.
I need the following headings:
About Me
My Services
Events
Blog
I don't need them to be seperate pages but if they can link to further down the page that would be great.
Industry/Entity Type
Personal Trainer
Coding
Coded - Design and coding required
Number of Pages Required
1 page
Requirements
Must have
- I need the following headings:
- About Me
- My Services
- Events
- Blog
- mobile friendly formatting
- health and fitness related photography
- Colour scheme in keeping with my existing logo

```html
<!DOCTYPE html>
<html lang="en">
<head>
<meta charset="utf-8">
<title>Marlowe Grant – Personal Training</title>
<link href="https://fonts.googleapis.com/css2?family=Open+Sans:wght@400;600;700&display=swap" rel="stylesheet">
<style>
:root{
  --orange:#f39325;
  --ink:#222222;
  --text:#555555;
  --muted:#777777;
  --panel:#f1f1f1;
  --panel-soft:#f5f5f5;
  --card:#eeeeee;
  --white:#ffffff;
  --footer:#353535;
  --footer-line:#4a4a4a;
}
*{margin:0;padding:0;box-sizing:border-box}
html,body{width:1200px;height:3315px;overflow:hidden}
body{font-family:"Open Sans",Arial,sans-serif;color:var(--text);background:var(--white);position:relative}
a{color:inherit;text-decoration:none}

/* Header */
.site-header{position:absolute;top:0;left:0;width:1200px;height:180px;background:var(--white)}
.brand{position:absolute;left:130px;top:98px;display:flex;align-items:center;gap:12px}
.brand-mark{width:22px;height:22px;border-radius:50%;background:var(--orange)}
.brand-name{font-size:27px;font-weight:600;color:var(--orange);letter-spacing:.3px}
.header-phone{position:absolute;right:132px;top:46px;font-size:24px;color:var(--ink);display:flex;align-items:center;gap:10px}
.main-nav{position:absolute;right:132px;top:122px;display:flex;gap:38px;font-size:13.5px;color:var(--ink)}
.main-nav .is-active{color:var(--orange)}

/* Hero */
.hero{position:absolute;top:180px;left:0;width:1200px;height:435px;background:linear-gradient(180deg,#c9ccce 0%,#9ea2a5 45%,#6e6a66 100%)}
.hero-arrow{position:absolute;top:202px;width:26px;height:30px;background:#2b2b2b;display:flex;align-items:center;justify-content:center}
.hero-arrow.prev{left:0}.hero-arrow.next{right:0}
.btn-join{position:absolute;left:530px;top:338px;width:140px;height:50px;background:var(--orange);color:var(--white);font-size:15px;font-weight:700;display:flex;align-items:center;justify-content:center;border-radius:3px;box-shadow:0 3px 6px rgba(0,0,0,.25)}

/* About */
.about{position:absolute;top:615px;left:0;width:1200px;height:615px}
.about-photo{position:absolute;left:0;top:0;width:600px;height:615px;background:linear-gradient(160deg,#8a6b4a 0%,#7fa7b2 22%,#a9c2c7 45%,#d9c9ae 75%,#cdb894 100%)}
.about-body{position:absolute;left:600px;top:0;width:600px;height:615px;background:var(--panel);padding:72px 120px 0 48px}
.section-title{font-size:38px;font-weight:700;color:var(--orange);text-transform:uppercase;letter-spacing:.5px;line-height:1}
.about-body p{font-size:11.5px;line-height:19px;color:var(--text);margin-top:22px}
.about-body .section-title+p{margin-top:30px}
.btn-outline{display:inline-flex;align-items:center;justify-content:center;width:97px;height:44px;margin-top:40px;background:var(--white);border:1px solid #d6d6d6;font-size:10.5px;color:var(--muted)}

/* Services */
.services{position:absolute;top:1230px;left:0;width:1200px;height:613px}
.services-body{position:absolute;left:0;top:0;width:600px;height:613px;background:var(--panel);padding:70px 0 0 133px}
.services-photo{position:absolute;left:600px;top:0;width:600px;height:613px;background:linear-gradient(120deg,#7a5a3f 0%,#a89a8a 35%,#5a5854 60%,#e3e3e3 100%)}
.service-list{list-style:none;margin-top:30px}
.service{display:flex;gap:16px;margin-bottom:35px}
.service-icon{flex:none;width:62px;height:62px;border-radius:50%;background:var(--white);display:flex;align-items:center;justify-content:center}
.service h3{font-size:19px;font-weight:600;color:var(--ink);margin-top:2px}
.service p{font-size:11.5px;line-height:17px;color:var(--muted);margin-top:6px;width:360px}

/* Events */
.events{position:absolute;top:1843px;left:0;width:1200px;height:527px;background:var(--white);text-align:center}
.events .section-title{margin-top:77px}
.events-intro{width:935px;margin:22px auto 0;font-size:11.5px;line-height:20px;color:var(--text)}
.event-cards{position:absolute;top:204px;left:133px;display:flex;gap:22px}
.event-card{width:297px;height:203px;background:var(--card);text-align:left;padding:22px 24px}
.event-card h4{font-size:14.5px;font-weight:400;line-height:21px;color:var(--ink)}
.event-date{font-size:14px;color:var(--orange);margin-top:12px}
.event-card p{font-size:10px;line-height:14px;color:var(--text);margin-top:12px}
.event-card p b{color:var(--ink);font-weight:700}
.slider-dots{position:absolute;top:437px;left:0;width:1200px;display:flex;justify-content:center;gap:10px}
.slider-dots span{width:12px;height:12px;border-radius:50%;background:#cfcfcf}
.slider-dots .is-active{background:var(--orange)}

/* Blog */
.blog{position:absolute;top:2370px;left:0;width:1200px;height:705px;background:var(--panel-soft);text-align:center}
.blog .section-title{margin-top:72px}
.blog-cards{position:absolute;top:146px;left:133px;display:flex;gap:46px}
.blog-card{width:444px;height:464px;background:var(--white)}
.blog-image{height:322px}
.blog-image.kettlebells{background:linear-gradient(160deg,#c9ccd0 0%,#a4a9ae 50%,#3a3c40 100%)}
.blog-image.pullups{background:radial-gradient(circle at 50% 40%,#6b6b6b 0%,#2a2a2a 55%,#111 100%)}
.blog-card p{font-size:14.5px;line-height:24px;color:var(--ink);padding:22px 30px 0}
.blog-card .read-more{display:inline-block;font-size:10px;color:var(--orange);margin-top:10px;text-decoration:underline}
.blog-arrow{position:absolute;top:368px}
.blog-arrow.prev{left:46px}.blog-arrow.next{right:46px}

/* Footer */
.site-footer{position:absolute;top:3075px;left:0;width:1200px;height:240px;background:var(--footer);color:var(--white)}
.footer-contacts{position:absolute;top:50px;left:133px;width:935px;display:flex;align-items:center;font-size:12.5px}
.footer-contacts .item{display:flex;align-items:center;gap:8px}
.footer-contacts .address{width:383px}
.footer-contacts .phone{width:175px}
.footer-social{margin-left:auto;display:flex;gap:20px}
.footer-social span{width:14px;height:14px;border-radius:50%;background:var(--white)}
.footer-rule{position:absolute;top:109px;left:133px;width:935px;height:1px;background:var(--footer-line)}
.footer-nav{position:absolute;top:149px;left:0;width:1200px;text-align:center;font-size:11px;word-spacing:4px}
.copyright{position:absolute;top:175px;left:0;width:1200px;text-align:center;font-size:11px}
</style>
</head>
<body>

<header class="site-header">
  <a class="brand" href="#top"><span class="brand-mark"></span><span class="brand-name">Marlowe Grant</span></a>
  <div class="header-phone">
    <svg width="14" height="22" viewBox="0 0 14 22"><rect x="1" y="1" width="12" height="20" rx="2" fill="none" stroke="#222" stroke-width="2"/><rect x="5" y="17" width="4" height="1.6" fill="#222"/></svg>
    555 010 2841
  </div>
  <nav class="main-nav">
    <a class="is-active" href="#top">Home</a>
    <a href="#about">About Me</a>
    <a href="#services">My Services</a>
    <a href="#events">Events</a>
    <a href="#blog">Blog</a>
    <a href="#contact">Contact</a>
  </nav>
</header>

<section class="hero" role="img" aria-label="Group bodyweight training session with box jumps in a bright gym">
  <span class="hero-arrow prev"><svg width="10" height="12" viewBox="0 0 10 12"><path d="M7 1 2 6l5 5" fill="none" stroke="#fff" stroke-width="2"/></svg></span>
  <span class="hero-arrow next"><svg width="10" height="12" viewBox="0 0 10 12"><path d="M3 1l5 5-5 5" fill="none" stroke="#fff" stroke-width="2"/></svg></span>
  <a class="btn-join" href="#contact">JOIN NOW</a>
</section>

<section class="about" id="about">
  <div class="about-photo" role="img" aria-label="Trainer walking along a sandy beach by the sea"></div>
  <div class="about-body">
    <h2 class="section-title">About Me</h2>
    <p>Nullam lorem urna, tempus eget mollis et, dapibus ac sem. Suspendisse gravida ornare erat sed pulvinar. Vestibulum luctus ex in egestas fringilla. Fusce nec leo ac urna pulvinar auctor. Mauris bibendum fringilla velit. Nulla in lorem at massa pellentesque posuere. Nulla tristique posuere molestie. Aliquam erat volutpat. Etiam quis aliquet risus. Duis ornare erat eget magna dapibus, in accumsan quam pharetra.</p>
    <p>Nam tempus, quam in bibendum vulputate, sapien dolor viverra nisl, vitae euismod elit turpis et nulla. Aliquam erat volutpat. Pellentesque blandit lacus eget nunc faucibus, et tincidunt eros viverra. Phasellus consequat sagittis nisi suscipit feugiat. Cras eget leo sed nunc hendrerit ultricies eu at nisl. Praesent iaculis faucibus urna sit amet lacinia. Maecenas consequat justo enim, ac mattis massa imperdiet quis. Fusce eget neque elit. Sed augue orci, elementum in magna congue, tincidunt vulputate erat. Aliquam consectetur orci molestie dictum molestie. Proin eget congue nulla, vel tempor diam.</p>
    <a class="btn-outline" href="#about">Read more</a>
  </div>
</section>

<section class="services" id="services">
  <div class="services-body">
    <h2 class="section-title">My Services</h2>
    <ul class="service-list">
      <li class="service">
        <span class="service-icon"><svg width="24" height="24" viewBox="0 0 24 24"><rect x="3" y="5" width="18" height="16" rx="2" fill="none" stroke="#f39325" stroke-width="2"/><path d="M3 10h18M8 3v4M16 3v4" stroke="#f39325" stroke-width="2"/></svg></span>
        <div><h3>Weight Loss</h3><p>Vestibulum condimentum, risus ut posuere cursus, velit justo accumsan sem, lobortis aliquet metus dui eu libero.</p></div>
      </li>
      <li class="service">
        <span class="service-icon"><svg width="24" height="24" viewBox="0 0 24 24"><path d="M14 2 5 14h6l-2 8 9-12h-6z" fill="#f39325"/></svg></span>
        <div><h3>Stamina</h3><p>Vestibulum condimentum, risus ut posuere cursus, velit justo accumsan sem, lobortis aliquet metus dui eu libero.</p></div>
      </li>
      <li class="service">
        <span class="service-icon"><svg width="24" height="24" viewBox="0 0 24 24"><circle cx="12" cy="14" r="8" fill="none" stroke="#f39325" stroke-width="2"/><path d="M12 14V9M10 3h4M12 3v3" stroke="#f39325" stroke-width="2"/></svg></span>
        <div><h3>Sports Fitness</h3><p>Vestibulum condimentum, risus ut posuere cursus, velit justo accumsan sem, lobortis aliquet metus dui eu libero.</p></div>
      </li>
      <li class="service">
        <span class="service-icon"><svg width="24" height="24" viewBox="0 0 24 24"><path d="M12 21 3.5 12.5A5 5 0 0 1 12 6a5 5 0 0 1 8.5 6.5z" fill="#f39325"/></svg></span>
        <div><h3>Healthy Lifestyle</h3><p>Vestibulum condimentum, risus ut posuere cursus, velit justo accumsan sem, lobortis aliquet metus dui eu libero.</p></div>
      </li>
    </ul>
  </div>
  <div class="services-photo" role="img" aria-label="Man holding a forearm plank on a gym floor"></div>
</section>

<section class="events" id="events">
  <h2 class="section-title">Events</h2>
  <p class="events-intro">Fusce sollicitudin lorem et luctus volutpat. Proin placerat dapibus gravida. In tristique tristique nulla eget hendrerit. Maecenas vel tortor accumsan quam varius imperdiet et vel eget elit. Aenean facilisis tincidunt lectus, id dictum nisi luctus eget. Vivamus efficitur ex condimentum, malesuada eros.</p>
  <div class="event-cards">
    <article class="event-card">
      <h4>Etiam mattis augue vehicula odio posuere, tempus lectus luctus.</h4>
      <div class="event-date">21 October, 2017</div>
      <p>Aliquam erat volutpat. Quisque aliquet ex nec est vestibulum pulvinar. Pellentesque convallis molestie enim sit amet efficitur. Etiam id imperdiet lectus. Vivamus lacus justo. <b>More</b></p>
    </article>
    <article class="event-card">
      <h4>Etiam mattis augue vehicula odio posuere, tempus lectus luctus.</h4>
      <div class="event-date">21 October, 2017</div>
      <p>Aliquam erat volutpat. Quisque aliquet ex nec est vestibulum pulvinar. Pellentesque convallis molestie enim sit amet efficitur. Etiam id imperdiet lectus. Vivamus lacus justo. <b>More</b></p>
    </article>
    <article class="event-card">
      <h4>Etiam mattis augue vehicula odio posuere, tempus lectus luctus.</h4>
      <div class="event-date">21 October, 2017</div>
      <p>Aliquam erat volutpat. Quisque aliquet ex nec est vestibulum pulvinar. Pellentesque convallis molestie enim sit amet efficitur. Etiam id imperdiet lectus. Vivamus lacus justo. <b>More</b></p>
    </article>
  </div>
  <div class="slider-dots"><span class="is-active"></span><span></span><span></span><span></span></div>
</section>

<section class="blog" id="blog">
  <h2 class="section-title">Blog</h2>
  <span class="blog-arrow prev"><svg width="14" height="24" viewBox="0 0 14 24"><path d="M12 2 2 12l10 10" fill="none" stroke="#999" stroke-width="2"/></svg></span>
  <div class="blog-cards">
    <article class="blog-card">
      <div class="blog-image kettlebells" role="img" aria-label="Kettlebells and a barbell resting on a gym floor"></div>
      <p>Pellentesque blandit lacus eget nunc faucibus, et tincidunt eros viverra. Phasellus consequat sagittis nisi suscipit feugia</p>
      <a class="read-more" href="#blog">Read more</a>
    </article>
    <article class="blog-card">
      <div class="blog-image pullups" role="img" aria-label="Athlete doing pull-ups in a dark gym"></div>
      <p>Etiam mattis augue vehicula odio posuere, sit amet tempus lectus luctus. Nulla facilisi. Etiam vel massa elementum, bibendum tellus.</p>
      <a class="read-more" href="#blog">Read more</a>
    </article>
  </div>
  <span class="blog-arrow next"><svg width="14" height="24" viewBox="0 0 14 24"><path d="M2 2l10 10L2 22" fill="none" stroke="#999" stroke-width="2"/></svg></span>
</section>

<footer class="site-footer" id="contact">
  <div class="footer-contacts">
    <span class="item address"><svg width="10" height="14" viewBox="0 0 10 14"><path d="M5 0a5 5 0 0 1 5 5c0 4-5 9-5 9S0 9 0 5a5 5 0 0 1 5-5z" fill="#fff"/><circle cx="5" cy="5" r="2" fill="#353535"/></svg>24 Building name, Street name, City - Zipcode</span>
    <span class="item phone"><svg width="8" height="13" viewBox="0 0 8 13"><rect x="0.8" y="0.8" width="6.4" height="11.4" rx="1.2" fill="none" stroke="#fff" stroke-width="1.4"/></svg>555 010 7730</span>
    <span class="item"><svg width="13" height="10" viewBox="0 0 13 10"><rect width="13" height="10" rx="1" fill="#fff"/><path d="M0.5 1 6.5 5.5 12.5 1" fill="none" stroke="#353535" stroke-width="1.2"/></svg>info@marlowegrant.com</span>
    <span class="footer-social" aria-label="Social links"><span></span><span></span><span></span><span></span></span>
  </div>
  <div class="footer-rule"></div>
  <nav class="footer-nav">Home &nbsp;| &nbsp;About Me &nbsp;| &nbsp;My Services &nbsp;| &nbsp;Events &nbsp;| &nbsp;Blog &nbsp;| &nbsp;Contact</nav>
  <p class="copyright">Copyright © 2017 Marlowe Grant. All rights reserved.</p>
</footer>

</body>
</html>
```